New Massage Business needs a Card design

We need a card design for our new massage therapy business based in Sydney, Au. The business is getting a makeover, so a little later on we'll need shirts, various pamphlets and promotional flyers, and possibly a website. The winner will be offered those jobs as well.

Colour scheme should be green, black, and steel/charcoal grey. The business focuses on massage as an anatomical solution to stress, muscle aches, pains and fatigue. Ideally we'd like an anatomical image of the muscle system (ref to the attached files). In my mind this image takes up most of the left third of the card, and shows points of tension and pain at the neck and lower back. This image should be the grey portion of the card.

On the upper right is the other image attached, with a simple line drawing of a vehicle on the left end of the line, and a building on the right end replacing the stick figure (we have a therapist specializing in mobile massage). The blank part in the middle of the line should have "Kestrel Wellness", and in smaller writing below, "The Tension Fix".

Bottom right corner should have the contact and business details.
On the back we'd like a "next appointment" and "refer a friend" option.

If you have a design which doesn't fit the above, but you feel suits the business, please submit anyway - sometimes you don't know what you like until you see it.

Business Details:
Name: Kestrel Wellness - The Tension Fix

Industry/Entity Type

Massage Therapy

Contact Information for Business Card

Business Details:
Contact name: Marcus
Title: Massage Therapist
Contact: 0458203617
Email: info@ktfbodywork.example

Requirements
Must have
• Colour scheme should be green, black, and steel/charcoal grey. The business focuses on massage as an anatomical solution to stress, muscle aches, pains and fatigue. Ideally we'd like an anatomical image of the muscle system (ref to the attached files). In my mind this image takes up most of the left third of the card, and shows points of tension and pain at the neck and lower back. This image should be the grey portion of the card.
• On the upper right is the other image attached, with a simple line drawing of a vehicle on the left end of the line, and a building on the right end replacing the stick figure (we have a therapist specializing in mobile massage). The blank part in the middle of the line should have "Kestrel Wellness", and in smaller writing below, "The Tension Fix".
• Bottom right corner should have the contact and business details.
• On the back we'd like a "next appointment" and "refer a friend" option.
Nice to have
• Matt finish - no gloss
• If you have a design which doesn't fit the above, but you feel suits the business, please submit anyway - sometimes you don't know what you like until you see it.
Should not have
• Anything 'Zen'. The business promotes the physiological and scientific benefits of massage. For clients with spiritual or meditative needs, we refer out.

```html
<!DOCTYPE html>
<html lang="en">
<head>
<meta charset="utf-8">
<title>Kestrel Wellness – Appointment Card (Back)</title>
<link rel="stylesheet" href="https://fonts.googleapis.com/css2?family=Montserrat:wght@300;400&display=swap">
<style>
  :root {
    --card-black: #111111;
    --steel-grey: #606060;
    --accent-green: #9ee000;
    --brand-white: #eeeeee;
    --font-main: "Montserrat", sans-serif;
  }
  html, body {
    margin: 0;
    padding: 0;
    overflow: hidden;
    background: var(--card-black);
  }
  .card {
    position: relative;
    width: 1200px;
    height: 758px;
    background: var(--card-black);
    overflow: hidden;
    font-family: var(--font-main);
    font-weight: 300;
    color: var(--accent-green);
  }
  .card__curve {
    position: absolute;
    inset: 0;
    width: 1200px;
    height: 758px;
  }
  .section-title {
    position: absolute;
    top: 44px;
    margin: 0;
    font-size: 36px;
    font-weight: 300;
    line-height: 1;
    letter-spacing: 0.5px;
  }
  .section-title--appointment { left: 50px; }
  .section-title--referral { right: 61px; }

  .field {
    position: absolute;
    display: flex;
    align-items: flex-end;
  }
  .field__label {
    font-size: 16px;
    line-height: 1;
    padding-bottom: 4px;
  }
  .field__line {
    position: absolute;
    height: 0;
    border-top: 1.5px solid var(--accent-green);
  }
  .field__suffix {
    position: absolute;
    font-size: 24px;
    line-height: 1;
  }

  .brand {
    position: absolute;
    right: 51px;
    top: 619px;
    text-align: center;
    color: var(--brand-white);
  }
  .brand__name {
    margin: 0;
    font-size: 40px;
    font-weight: 300;
    line-height: 1;
    letter-spacing: 0.5px;
  }
  .brand__tagline {
    margin: 6px 0 0;
    font-size: 27px;
    font-weight: 300;
    line-height: 1;
  }
</style>
</head>
<body>
<main class="card">
  <svg class="card__curve" viewBox="0 0 1200 758" aria-hidden="true">
    <path d="M202 758 Q700 560 1200 248 L1200 758 Z" fill="var(--steel-grey)"/>
  </svg>

  <h2 class="section-title section-title--appointment">NEXT APPOINTMENT</h2>
  <h2 class="section-title section-title--referral">REFER A FRIEND</h2>

  <!-- Next appointment fields -->
  <div class="field" style="left:29px; top:134px;">
    <span class="field__label">Name:</span>
  </div>
  <div class="field__line" style="left:95px; width:330px; top:152px;"></div>

  <div class="field" style="left:29px; top:193px;">
    <span class="field__label">At:</span>
  </div>
  <div class="field__line" style="left:96px; width:329px; top:212px;"></div>
  <span class="field__suffix" style="left:439px; top:193px;">AM/PM</span>

  <div class="field" style="left:29px; top:251px;">
    <span class="field__label">On:</span>
  </div>
  <div class="field__line" style="left:99px; width:328px; top:271px;"></div>

  <!-- Referral fields -->
  <div class="field" style="left:691px; top:132px;">
    <span class="field__label">Name:</span>
  </div>
  <div class="field__line" style="left:758px; width:387px; top:150px;"></div>

  <div class="field" style="left:691px; top:190px;">
    <span class="field__label">Friend:</span>
  </div>
  <div class="field__line" style="left:760px; width:386px; top:210px;"></div>

  <div class="brand">
    <p class="brand__name">KESTREL WELLNESS</p>
    <p class="brand__tagline">The Tension Fix</p>
  </div>
</main>
</body>
</html>
```